Banner dimension 1767 X 887 for Tolvenko website

Need one banner for our website www.tolvenko.com.au, The dimension of the banner should be 1767 x 887. Attached to this brief are two images that needs to be on that one banner, PLEASE DO NOT SEND SEPARATE BANNERS, both images on the same banner. Thanks

The banner should have the following message on it:

1.) " Take a further 40% off all stock" ( use code: TOLVENKO. Ends 31/12/2015)
2.) " Kick back or kick it up a notch this Autumn in the most versatile pique striped polo shirts and Pinafore belt strap denim dress"

Target Market(s)

kids aged 5-12yrs

Requirements
Must have
• very playful

```html
<!DOCTYPE html>
<html lang="en">
<head>
<meta charset="utf-8">
<title>Tolvenko – Take a further 40% off all stock</title>
<link rel="stylesheet" href="https://fonts.googleapis.com/css2?family=Fira+Sans:wght@600;700;800&family=Alegreya+Sans+SC:wght@800;900&display=swap">
<style>
  :root {
    --sky-deep: #6fc3ee;
    --sky-mid: #a9dcf6;
    --sun-glow: #ffffff;
    --floor-dark: #2b1a12;
    --floor-mid: #3d271b;
    --promo-blue: #0fa2e2;
    --promo-green: #7cc242;
    --ink: #111111;
    --paper: #ffffff;
  }
  * { margin: 0; padding: 0; box-sizing: border-box; }
  html, body { width: 1200px; height: 602px; overflow: hidden; }
  body { background: var(--paper); }

  .banner {
    position: relative;
    width: 1200px;
    height: 602px;
    overflow: hidden;
    background:
      radial-gradient(ellipse 520px 360px at 640px 40px, var(--sun-glow) 0%, rgba(255,255,255,0.75) 35%, rgba(255,255,255,0) 100%),
      linear-gradient(180deg, var(--sky-mid) 0%, var(--sky-deep) 100%);
  }

  .sky-decor { position: absolute; inset: 0; }

  .floor {
    position: absolute;
    left: 0; right: 0; bottom: 0;
    height: 80px;
    background: linear-gradient(180deg, var(--floor-mid) 0%, var(--floor-dark) 100%);
  }

  .kids-photo {
    position: absolute;
    left: 105px;
    top: 118px;
    width: 430px;
    height: 455px;
    border-radius: 40% 40% 12px 12px / 30% 30% 12px 12px;
    background: linear-gradient(180deg, rgba(255,255,255,0.35) 0%, rgba(120,150,170,0.55) 45%, rgba(70,90,110,0.6) 100%);
  }

  .promo-code {
    position: absolute;
    left: 586px;
    top: 160px;
    font-family: "Fira Sans", sans-serif;
    font-weight: 700;
    font-size: 27px;
    color: var(--ink);
    transform: rotate(-3.5deg);
    transform-origin: left bottom;
    white-space: nowrap;
  }

  .promo-ends {
    position: absolute;
    left: 880px;
    top: 136px;
    width: 268px;
    height: 44px;
    background: var(--promo-green);
    transform: rotate(-3.5deg);
    font-family: "Fira Sans", sans-serif;
    font-weight: 600;
    font-size: 23px;
    color: var(--paper);
    display: flex;
    align-items: center;
    justify-content: center;
  }

  .promo-band {
    position: absolute;
    left: 436px;
    top: 226px;
    width: 800px;
    height: 50px;
    background: var(--promo-blue);
    transform-origin: 0 0;
    transform: rotate(-3.6deg);
    display: flex;
    align-items: center;
    padding-left: 94px;
  }

  .promo-headline {
    font-family: "Fira Sans", sans-serif;
    font-weight: 700;
    font-size: 32px;
    line-height: 1;
    color: var(--paper);
    text-transform: uppercase;
    white-space: nowrap;
    letter-spacing: 0.6px;
  }
  .promo-headline .promo-percent { font-size: 42px; font-weight: 800; }

  .tagline {
    position: absolute;
    left: 572px;
    top: 343px;
    font-family: "Alegreya Sans SC", sans-serif;
    font-weight: 900;
    font-size: 33px;
    line-height: 40px;
    letter-spacing: 1.7px;
    color: var(--ink);
  }
  .tagline-line { display: block; white-space: nowrap; }
</style>
</head>
<body>
  <main class="banner">
    <svg class="sky-decor" width="1200" height="602" viewBox="0 0 1200 602" aria-hidden="true">
      <g fill="#ffffff" opacity="0.18">
        <polygon points="640,40 300,0 360,0"/>
        <polygon points="640,40 470,0 520,0"/>
        <polygon points="640,40 700,0 760,0"/>
        <polygon points="640,40 880,0 960,0"/>
        <polygon points="640,40 1100,60 1100,110"/>
        <polygon points="640,40 200,140 220,180"/>
        <polygon points="640,40 420,330 460,340"/>
        <polygon points="640,40 820,330 860,320"/>
      </g>
      <g fill="#ffffff" opacity="0.55">
        <circle cx="410" cy="122" r="16"/>
        <circle cx="471" cy="127" r="17"/>
        <circle cx="440" cy="182" r="15"/>
        <circle cx="521" cy="172" r="12"/>
        <circle cx="675" cy="305" r="20"/>
        <circle cx="752" cy="303" r="13"/>
        <circle cx="1102" cy="305" r="14"/>
        <circle cx="993" cy="97" r="15"/>
        <circle cx="1010" cy="120" r="19"/>
        <circle cx="1125" cy="70" r="16"/>
        <circle cx="1185" cy="36" r="18"/>
        <circle cx="1030" cy="260" r="16"/>
        <circle cx="300" cy="180" r="12"/>
      </g>
      <g fill="#ffffff" opacity="0.6">
        <ellipse cx="110" cy="280" rx="45" ry="18"/>
        <ellipse cx="120" cy="60" rx="110" ry="40"/>
        <ellipse cx="1160" cy="250" rx="50" ry="16"/>
      </g>
    </svg>

    <div class="floor"></div>

    <div class="kids-photo" role="img" aria-label="Photo of a smiling girl in a denim pinafore dress and a boy in a striped polo shirt and denim shorts, posing playfully"></div>

    <div class="promo-band">
      <p class="promo-headline">Take a further <span class="promo-percent">40%</span> off all stock</p>
    </div>

    <p class="promo-code">use code: TOLVENKO</p>
    <p class="promo-ends">Ends 31/12/2015</p>

    <p class="tagline">
      <span class="tagline-line">Kick back or kick it up a notch this</span>
      <span class="tagline-line">Autumn in the most versatile pique</span>
      <span class="tagline-line">striped polo shirts and Pinafore</span>
      <span class="tagline-line">belt strap denim dress</span>
    </p>
  </main>
</body>
</html>
```